Front & Back Book Cover Design

Title:
THE QUIET LANDLORD: How to Grow Comfort and Capital Through Property You Merely Guide
Author:
Wes T. Marlund
Design Philosophy:
A modern, minimalist-luxury aesthetic that feels visionary and intelligent — positioned between business innovation (The Nimble Venture), modern finance (The Temperament of Wealth), and timeless real estate insight (Bold Uncle Meek Uncle).
Think: clean, bold, and idea-driven — a visual reflection of the book’s central concept: wealth through clarity, not clutter.
Back Cover:
To include book description along with author photo and bio
Files:
PNG, PDF, EPUB

```html
<!DOCTYPE html>
<html lang="en">
<head>
<meta charset="utf-8">
<title>The Quiet Landlord — Cover Spread</title>
<link rel="stylesheet" href="https://fonts.googleapis.com/css2?family=Oswald:wght@500;600&family=Inter:wght@400;600&family=Montserrat:wght@500;800&display=swap">
<style>
  :root {
    --stage: #cfcfcf;
    --cover: #0c0c0c;
    --white: #ffffff;
    --text: #e9e9e9;
    --gold: #f2c53d;
    --art-light: #5a5a5a;
    --art-dark: #1e1e1e;
    --photo-a: #6b6660;
    --photo-b: #2a2622;
  }
  * { box-sizing: border-box; margin: 0; padding: 0; }
  html, body { width: 832px; height: 1200px; overflow: hidden; }
  body { background: var(--stage); position: relative; font-family: "Inter", Arial, sans-serif; }

  .spread {
    position: absolute; left: 0; top: 312px;
    width: 832px; height: 576px;
    background: var(--cover);
    color: var(--text);
  }

  /* Back cover */
  .back { position: absolute; left: 0; top: 0; width: 396px; height: 576px; }
  .back-title {
    position: absolute; left: 0; width: 384px; top: 26px;
    text-align: center; font-family: "Oswald", "Arial Narrow", sans-serif;
    font-weight: 500; font-size: 24px; color: var(--white); letter-spacing: 0.2px;
  }
  .gold { color: var(--gold); }
  .blurb {
    position: absolute; left: 32px; top: 66px; width: 322px;
    font-size: 10.8px; line-height: 12.8px; letter-spacing: -0.15px; color: var(--text);
  }
  .blurb p { margin-bottom: 8px; text-align: justify; hyphens: auto; }
  .blurb .hook { font-size: 12.4px; line-height: 15px; text-align: left; color: var(--white); letter-spacing: 0; }
  .blurb ul { list-style: none; margin: -7px 0 8px; }
  .blurb li { padding-left: 9px; text-indent: -9px; }
  .blurb li::before { content: "• "; }
  .blurb strong { font-weight: 600; color: var(--white); }

  .author-box { position: absolute; left: 32px; top: 454px; width: 320px; display: flex; gap: 9px; }
  .author-photo {
    flex: 0 0 68px; height: 88px; border: 1px solid var(--gold);
    background: linear-gradient(160deg, var(--photo-a), var(--photo-b));
  }
  .author-bio { font-size: 8.9px; line-height: 10.7px; letter-spacing: -0.1px; text-align: justify; }
  .author-bio h3 { font-size: 9.2px; font-weight: 600; color: var(--gold); margin-bottom: 1px; letter-spacing: 0; }

  /* Spine */
  .spine {
    position: absolute; left: 396px; top: 0; width: 52px; height: 576px;
    display: flex; justify-content: center; padding-top: 30px;
  }
  .spine-text {
    writing-mode: vertical-rl; display: flex; align-items: center; gap: 24px;
    white-space: nowrap;
  }
  .spine-title { font-family: "Oswald", "Arial Narrow", sans-serif; font-weight: 600; font-size: 30px; color: var(--white); }
  .spine-author { font-family: "Montserrat", Arial, sans-serif; font-weight: 800; font-size: 24px; color: var(--white); }

  /* Front cover */
  .front { position: absolute; left: 448px; top: 0; width: 384px; height: 576px; text-align: center; }
  .front-the {
    position: absolute; top: 26px; left: 0; width: 384px;
    display: flex; justify-content: center; align-items: center; gap: 6px;
    font-family: "Oswald", "Arial Narrow", sans-serif; font-weight: 500; font-size: 42px; color: var(--white);
  }
  .front-the::before, .front-the::after { content: ""; width: 50px; height: 1.5px; background: var(--white); }
  .front-kicker {
    position: absolute; top: 74px; left: 0; width: 384px;
    font-family: "Montserrat", Arial, sans-serif; font-weight: 500; font-size: 48px;
    letter-spacing: 22px; padding-left: 22px; color: var(--gold); line-height: 1;
  }
  .front-main {
    position: absolute; top: 120px; left: 0; width: 384px;
    font-family: "Oswald", "Arial Narrow", sans-serif; font-weight: 600; font-size: 82px;
    line-height: 1; color: var(--white); letter-spacing: -0.5px;
  }
  .front-subtitle {
    position: absolute; top: 218px; left: 0; width: 384px;
    font-size: 14.4px; line-height: 17.5px; color: var(--text);
  }
  .cover-art {
    position: absolute; left: 60px; top: 258px; width: 264px; height: 268px;
    background: linear-gradient(180deg, var(--art-light), var(--art-dark));
  }
  .front-author {
    position: absolute; top: 532px; left: 0; width: 384px;
    font-family: "Montserrat", Arial, sans-serif; font-weight: 800; font-size: 22px;
    letter-spacing: 4px; color: var(--gold);
  }
</style>
</head>
<body>
  <main class="spread">
    <section class="back">
      <h2 class="back-title">THE <span class="gold">QUIET</span> LANDLORD</h2>
      <div class="blurb">
        <p class="hook">What if the smartest real estate investors in the world don’t actually own anything?</p>
        <p>In a world where leverage has replaced labor and access has replaced assets, The Quiet Landlord reveals how a new generation of entrepreneurs is building wealth without deeds, mortgages, or massive capital.</p>
        <p>Wes T. Marlund exposes the hidden playbook behind modern real estate wealth — not through ownership, but through control, creativity, and influence.</p>
        <p>You’ll discover how to:</p>
        <ul>
          <li><strong>Profit from properties you never buy</strong> through partnerships, performance models, and control agreements.</li>
          <li><strong>Monetize your skills, systems, and relationships</strong> just like institutional investors do.</li>
          <li><strong>Build digital real estate</strong> — brands, websites, and lead funnels that pay like rentals.</li>
          <li><strong>Create recurring income</strong> through master leases, management contracts, and service-based equity.</li>
          <li><strong>Design your freedom formula</strong> — where wealth is measured in time, not titles.</li>
        </ul>
        <p>Packed with frameworks, examples, and the mindset of modern deal-makers, The Quiet Landlord is a blueprint for the future of wealth creation — one built on access, not assets.</p>
        <p>Because in the new economy, <strong>the most powerful investors don’t own real estate. They own opportunity.<br>And now, you can too.</strong></p>
      </div>
      <div class="author-box">
        <div class="author-photo" role="img" aria-label="Portrait photo of the author"></div>
        <div class="author-bio">
          <h3>About the Author</h3>
          <p>Wes T. Marlund is a real estate entrepreneur and owner of Harlowe Crest Designs in Las Vegas, NV and Northgate Realty Partners in Ventura, California. Combining design, development, and deal strategy, he’s helped agents, investors, and entrepreneurs build freedom through systems — not stuff. The Quiet Landlord is his definitive guide to building wealth through creative control.</p>
        </div>
      </div>
    </section>

    <section class="spine">
      <div class="spine-text">
        <span class="spine-title">THE <span class="gold">QUIET</span> LANDLORD</span>
        <span class="spine-author">WES T. MARLUND</span>
      </div>
    </section>

    <section class="front">
      <div class="front-the">THE</div>
      <div class="front-kicker">QUIET</div>
      <h1 class="front-main">LANDLORD</h1>
      <p class="front-subtitle">How to Grow Comfort and Capital Through<br>Property You Merely Guide</p>
      <div class="cover-art" role="img" aria-label="Cover illustration of a city skyline"></div>
      <div class="front-author">WES T. MARLUND</div>
    </section>
  </main>
</body>
</html>
```